Need a business card for our overland brand!

We had the logo made and we need a great design for our business card. Use the logo provide or tweak it however you see fit.

Contact Information for Business Card

Name, Title, Telephone, email, website

```html
<!DOCTYPE html>
<html lang="en">
<head>
<meta charset="utf-8">
<title>Summit Trail Co — Business Card</title>
<link href="https://fonts.googleapis.com/css2?family=Montserrat:wght@400;700;800&family=Roboto:wght@400&display=swap" rel="stylesheet">
<style>
  :root {
    --bg: #d3d6d8;
    --paper: #f1f1ef;
    --navy: #16213a;
    --blue: #1f8fb8;
    --ink: #2a2d33;
    --rule: #8d9096;
  }
  * { box-sizing: border-box; margin: 0; padding: 0; }
  html, body { width: 1200px; height: 1049px; overflow: hidden; background: var(--bg); }
  .stage {
    position: relative; width: 1200px; height: 1049px;
    display: flex; align-items: center; justify-content: center; gap: 40px;
  }
  .card {
    width: 540px; height: 309px; position: relative;
    box-shadow: 0 10px 24px rgba(0,0,0,.18);
  }
  .card--front { background: var(--paper); border-bottom: 4px solid var(--blue); }
  .card--back { background: var(--navy); border-bottom: 4px solid var(--blue);
    display: flex; align-items: center; justify-content: center; }

  .brand {
    font-family: "Montserrat", sans-serif; font-weight: 800;
    text-transform: uppercase; line-height: .95; letter-spacing: .5px;
  }
  .card--front .brand {
    position: absolute; left: 40px; top: 62px; width: 200px;
    font-size: 40px; color: var(--navy); text-align: center;
  }
  .card--back .brand { font-size: 68px; color: var(--paper); text-align: center; }

  .divider { position: absolute; left: 262px; top: 60px; width: 1px; height: 140px; background: var(--rule); }

  .details { position: absolute; left: 284px; top: 62px; font-family: "Roboto", sans-serif; color: var(--ink); }
  .details__name { font-family: "Montserrat", sans-serif; font-weight: 700; font-size: 17px; color: var(--navy); letter-spacing: .5px; }
  .details__title { font-family: "Montserrat", sans-serif; font-weight: 400; font-size: 14px; color: var(--blue); margin-bottom: 14px; }
  .contact { list-style: none; font-size: 14px; }
  .contact li { display: flex; align-items: center; gap: 8px; height: 21px; }
  .contact svg { width: 13px; height: 13px; fill: var(--blue); flex: none; }

  .address {
    position: absolute; left: 40px; bottom: 38px;
    display: flex; align-items: center; gap: 8px;
    font-family: "Roboto", sans-serif; font-size: 14px; color: var(--ink);
  }
  .address svg { width: 12px; height: 16px; fill: var(--blue); }
</style>
</head>
<body>
<main class="stage">
  <section class="card card--front">
    <div class="brand">Summit<br>Trail Co</div>
    <div class="divider"></div>
    <div class="details">
      <p class="details__name">DALEN RUSKIN</p>
      <p class="details__title">Founder &amp; CEO</p>
      <ul class="contact">
        <li><svg viewBox="0 0 16 16"><path d="M3 1l3 3-2 2a10 10 0 0 0 6 6l2-2 3 3-2 2C7 15 1 9 1 3z"/></svg>555.014.2290</li>
        <li><svg viewBox="0 0 16 16"><path d="M1 3h14v10H1z M1 3l7 6 7-6" /></svg>info@summittrailco.com</li>
        <li><svg viewBox="0 0 16 16"><circle cx="8" cy="8" r="7"/></svg>www.summittrailco.com</li>
      </ul>
    </div>
    <p class="address">
      <svg viewBox="0 0 12 16"><path d="M6 0a6 6 0 0 0-6 6c0 4.5 6 10 6 10s6-5.5 6-10a6 6 0 0 0-6-6zm0 8.5A2.5 2.5 0 1 1 6 3.5a2.5 2.5 0 0 1 0 5z"/></svg>
      Harlow Ave Ste 200 PMB 418207 Austin, TX 78701
    </p>
  </section>
  <section class="card card--back">
    <div class="brand">Summit<br>Trail Co</div>
  </section>
</main>
</body>
</html>
```